App Design Project

Hello,
I'm looking for a great designer for my iOS Applications, we have a lot of works and we're short in designers :(
I want to revamp my thermometer iOS app. You will find attached the images I want to replace. I need something with the same element (temp, condition, weather icon) but with a different look!
Same, new icon, you have carte blanche to this one.
I want a design that stands out from the hundreds of weather application that almost all the same design. I am looking for something that does say "wow, it rocks."
Please do not Provide classic design that we can see everywhere ... I'm looking for something with a real artistic choice, contrast, colours, etc.
As a marketing screenshot, I want something classic, you'll find an example attached, feel free to innovate.
To sum-up :
- One new view for my App
- One new icon
- One marketing screenshot
Marketing

```html
<!DOCTYPE html>
<html lang="en">
<head>
<meta charset="utf-8">
<title>Weather App – Snow View</title>
<link href="https://fonts.googleapis.com/css2?family=Advent+Pro:wght@200;300;400&family=Oswald:wght@500;600&display=swap" rel="stylesheet">
<style>
  :root {
    --bg: #55585c;
    --sky-top: #c9d3de;
    --sky-mid: #9fb0c2;
    --rock: #5d6a78;
    --snow-white: #ffffff;
    --tag-bg: rgba(60, 62, 66, 0.88);
    --panel-dark: rgba(24, 28, 34, 0.82);
    --accent: #27a3e8;
    --ring-track: #1e2126;
    --divider: rgba(255, 255, 255, 0.55);
    --label: #ffffff;
  }
  * { margin: 0; padding: 0; box-sizing: border-box; }
  html, body { width: 1200px; height: 1000px; overflow: hidden; }
  body {
    background: var(--bg);
    font-family: "Advent Pro", "Arial Narrow", sans-serif;
    color: var(--snow-white);
    position: relative;
  }

  /* ---------- App screen ---------- */
  .app-screen {
    position: absolute;
    left: 728px; top: 155px;
    width: 500px; height: 888px;
    overflow: hidden;
    transform: scale(0.768);
    transform-origin: 0 0;
  }
  .scenery {
    position: absolute; inset: 0;
    background:
      linear-gradient(180deg, var(--sky-top) 0%, #b7c4d2 25%, var(--sky-mid) 45%, #7f91a4 62%, var(--rock) 80%, #3f4955 100%);
  }
  .location-tag {
    position: absolute; right: 0; top: 17px;
    width: 147px; height: 38px;
    background: var(--tag-bg);
    font-family: "Oswald", sans-serif; font-weight: 500;
    font-size: 19px; letter-spacing: 0.5px;
    display: flex; align-items: center; justify-content: center;
  }
  .condition-icon {
    position: absolute; left: 141px; top: 148px; width: 220px; height: 180px;
  }
  .condition-name {
    position: absolute; left: 0; width: 100%; top: 362px;
    text-align: center; font-weight: 300; font-size: 82px; line-height: 1;
    letter-spacing: 2px;
  }
  .rule {
    position: absolute; left: 14px; width: 478px; height: 1px; background: var(--divider);
  }
  .rule--top { top: 471px; }
  .rule--bottom { top: 611px; }
  .current-temp {
    position: absolute; top: 480px; left: 0; width: 100%;
    display: flex; justify-content: center; align-items: center; gap: 10px;
  }
  .current-temp .thermo { width: 30px; height: 70px; }
  .current-temp .value { font-weight: 300; font-size: 112px; line-height: 1; letter-spacing: 4px; }
  .unit-toggle {
    position: absolute; left: 407px; top: 561px; width: 74px; height: 29px;
    background: #2a2d31; border-radius: 3px;
  }
  .unit-toggle .knob {
    position: absolute; left: 3px; top: 3px; width: 36px; height: 23px;
    background: linear-gradient(#f4f4f4, #cfcfcf); border-radius: 2px;
  }
  .unit-toggle .unit {
    position: absolute; right: 8px; top: 3px; color: var(--accent);
    font-family: "Oswald", sans-serif; font-size: 16px;
  }

  .conditions-bar {
    position: absolute; left: 0; top: 657px; width: 100%; height: 140px;
    background: var(--panel-dark);
    display: flex;
  }
  .conditions-bar .cell { display: flex; align-items: center; }
  .humidity { width: 216px; padding-left: 12px; gap: 12px; border-right: 1px solid rgba(255,255,255,0.3); }
  .wind { flex: 1; padding-left: 30px; gap: 22px; font-size: 40px; font-weight: 400; letter-spacing: 2px; }
  .ring { position: relative; width: 110px; height: 110px; }
  .ring span {
    position: absolute; inset: 0; display: flex; align-items: center; justify-content: center;
    font-size: 36px; font-weight: 400;
  }

  .forecast {
    position: absolute; left: 0; top: 797px; width: 100%; height: 91px;
    background: var(--accent);
    display: flex;
  }
  .forecast .day {
    flex: 1; display: flex; flex-direction: column; align-items: center; padding-top: 8px;
  }
  .day-name { font-size: 23px; font-weight: 400; letter-spacing: 1px; line-height: 1; }
  .day-detail { display: flex; align-items: center; gap: 6px; margin-top: 6px; }
  .day-detail svg.wx { width: 34px; height: 30px; }
  .temps { font-family: "Oswald", sans-serif; font-size: 14px; line-height: 17px; font-weight: 500; }
  .temps div { display: flex; align-items: center; gap: 3px; }

  /* ---------- Forecast callout ---------- */
  .callout {
    position: absolute; left: 310px; top: 618px; width: 344px; height: 344px;
    border-radius: 50%; background: var(--accent);
  }
  .callout .day-name {
    position: absolute; top: 48px; width: 100%; text-align: center;
    font-size: 50px; font-weight: 300;
  }
  .callout .wx { position: absolute; left: 120px; top: 104px; width: 96px; height: 82px; }
  .callout .reading {
    position: absolute; left: 122px; display: flex; align-items: center; gap: 16px;
    font-family: "Oswald", sans-serif; font-weight: 500; font-size: 38px; line-height: 40px;
    letter-spacing: 1px;
  }
  .callout .reading svg { width: 16px; height: 40px; }
  .reading--high { top: 210px; }
  .reading--low { top: 262px; }

  .legend {
    position: absolute; left: 150px; width: 278px; height: 28px;
    display: flex; align-items: center; gap: 9px;
    font-family: "Oswald", sans-serif; font-weight: 600; font-size: 21px; letter-spacing: 2px;
    color: var(--label); line-height: 1;
  }
  .legend i { display: block; flex: 1; height: 1px; background: var(--label); }
  .legend--high { top: 834px; }
  .legend--low { top: 882px; }
</style>
</head>
<body>

<svg width="0" height="0" style="position:absolute">
  <defs>
    <symbol id="thermo" viewBox="0 0 12 30">
      <rect x="3.5" y="1" width="5" height="20" rx="2.5" fill="none" stroke="#fff" stroke-width="1.6"/>
      <circle cx="6" cy="24" r="4.5" fill="#fff"/>
      <rect x="5" y="10" width="2" height="12" fill="#fff"/>
    </symbol>
    <symbol id="sun-cloud" viewBox="0 0 40 34">
      <g stroke="#fff" stroke-width="2.4" stroke-linecap="round" fill="none">
        <line x1="22" y1="2" x2="22" y2="6"/><line x1="31" y1="5" x2="29" y2="8"/>
        <line x1="36" y1="13" x2="32" y2="13"/><line x1="13" y1="5" x2="15" y2="8"/>
        <path d="M15 14a8 8 0 0 1 15 4"/>
        <path d="M9 31h20a6 6 0 0 0 0-12a9 9 0 0 0-17 2a5 5 0 0 0-3 10z" fill="var(--accent)"/>
      </g>
    </symbol>
    <symbol id="cloud" viewBox="0 0 40 34">
      <path d="M9 28h20a6 6 0 0 0 0-12a9 9 0 0 0-17 2a5 5 0 0 0-3 10z" fill="none" stroke="#fff" stroke-width="2.4"/>
    </symbol>
    <symbol id="storm" viewBox="0 0 40 34">
      <path d="M12 26h-3a5 5 0 0 1 3-10a9 9 0 0 1 17-2a6 6 0 0 1 0 12h-3" fill="none" stroke="#fff" stroke-width="2.4"/>
      <path d="M21 18l-5 8h5l-3 7" fill="none" stroke="#fff" stroke-width="2.2" stroke-linejoin="round"/>
    </symbol>
  </defs>
</svg>

<!-- Forecast callout -->
<div class="callout">
  <div class="day-name">MON</div>
  <svg class="wx"><use href="#sun-cloud"/></svg>
  <div class="reading reading--high"><svg><use href="#thermo"/></svg>25°</div>
  <div class="reading reading--low"><svg><use href="#thermo"/></svg>19°</div>
</div>
<div class="legend legend--high">High Temp<i></i></div>
<div class="legend legend--low">Low Temp<i></i></div>

<!-- App screen -->
<main class="app-screen">
  <div class="scenery" role="img" aria-label="Photograph of snow-covered mountain peaks under a cloudy sky"></div>

  <div class="location-tag">LONDON, UK</div>

  <svg class="condition-icon" viewBox="0 0 220 180" aria-label="Snow">
    <path d="M58 148h-8a40 40 0 0 1 4-80a58 58 0 0 1 108-14a44 44 0 0 1 8 94h-8"
          fill="none" stroke="#fff" stroke-width="16" stroke-linecap="round"/>
    <g fill="#fff" transform="translate(110 135)">
      <circle cx="0" cy="-17" r="10"/><circle cx="0" cy="17" r="10"/>
      <circle cx="-15" cy="-8.5" r="10"/><circle cx="15" cy="-8.5" r="10"/>
      <circle cx="-15" cy="8.5" r="10"/><circle cx="15" cy="8.5" r="10"/>
      <circle cx="0" cy="0" r="8"/>
    </g>
    <circle cx="110" cy="135" r="5" fill="#9fb0c2"/>
  </svg>

  <div class="condition-name">Snow</div>
  <div class="rule rule--top"></div>

  <div class="current-temp">
    <svg class="thermo"><use href="#thermo"/></svg>
    <span class="value">-5°C</span>
  </div>
  <div class="unit-toggle"><div class="knob"></div><span class="unit">°C</span></div>
  <div class="rule rule--bottom"></div>

  <section class="conditions-bar">
    <div class="cell humidity">
      <svg width="52" height="30" viewBox="0 0 52 30" aria-label="Wind">
        <g fill="none" stroke="#fff" stroke-width="4" stroke-linecap="round">
          <path d="M2 10h30a6 6 0 1 0-6-6"/>
          <path d="M2 18h40a6 6 0 1 1-6 6"/>
          <line x1="8" y1="26" x2="24" y2="26"/>
        </g>
      </svg>
      <div class="ring">
        <svg width="110" height="110" viewBox="0 0 110 110">
          <circle cx="55" cy="55" r="47" fill="none" stroke="var(--ring-track)" stroke-width="10"/>
          <circle cx="55" cy="55" r="47" fill="none" stroke="var(--accent)" stroke-width="10"
                  stroke-dasharray="88.6 206.7" transform="rotate(90 55 55)"/>
        </svg>
        <span>30 %</span>
      </div>
    </div>
    <div class="cell wind">
      <svg width="40" height="40" viewBox="0 0 40 40" aria-label="Wind direction">
        <circle cx="20" cy="20" r="17" fill="none" stroke="#fff" stroke-width="5"/>
        <path d="M20 10c-4 6-6 9-6 12a6 6 0 0 0 12 0c0-3-2-6-6-12z" fill="#fff"/>
      </svg>
      <span>N 39 km/h</span>
    </div>
  </section>

  <section class="forecast">
    <div class="day">
      <div class="day-name">MON</div>
      <div class="day-detail">
        <svg class="wx"><use href="#sun-cloud"/></svg>
        <div class="temps">
          <div><svg width="6" height="14"><use href="#thermo"/></svg>25°</div>
          <div><svg width="6" height="14"><use href="#thermo"/></svg>19°</div>
        </div>
      </div>
    </div>
    <div class="day">
      <div class="day-name">TUES</div>
      <div class="day-detail">
        <svg class="wx"><use href="#cloud"/></svg>
        <div class="temps">
          <div><svg width="6" height="14"><use href="#thermo"/></svg>19°</div>
          <div><svg width="6" height="14"><use href="#thermo"/></svg>14°</div>
        </div>
      </div>
    </div>
    <div class="day">
      <div class="day-name">WEDS</div>
      <div class="day-detail">
        <svg class="wx"><use href="#storm"/></svg>
        <div class="temps">
          <div><svg width="6" height="14"><use href="#thermo"/></svg>12°</div>
          <div><svg width="6" height="14"><use href="#thermo"/></svg>6°</div>
        </div>
      </div>
    </div>
    <div class="day">
      <div class="day-name">THURS</div>
      <div class="day-detail">
        <svg class="wx"><use href="#sun-cloud"/></svg>
        <div class="temps">
          <div><svg width="6" height="14"><use href="#thermo"/></svg>25°</div>
          <div><svg width="6" height="14"><use href="#thermo"/></svg>19°</div>
        </div>
      </div>
    </div>
  </section>
</main>

</body>
</html>
```